Ember Fold Whiskey Label

We are looking for a label to be made for our single batch whiskey. in the attached pdf you will see the lay out of the design. We are going to use a whiskey bottle with a cork. Some of the label you will need to leave some space for hand writing.

Target Market(s)

people who like craft beer and whiskey

Industry/Entity Type

Craft Distillery

Font styles to use
Decorative

Colors

Designer to choose colors to be used in the design.

Requirements
Must have
• room for hand writing informatiom

```html
<!DOCTYPE html>
<html lang="en">
<head>
<meta charset="utf-8">
<title>Ember Fold Whiskey Label</title>
<link rel="stylesheet" href="https://fonts.googleapis.com/css2?family=Rye&family=Old+Standard+TT:wght@400;700&display=swap">
<style>
  :root {
    --bg: #f4f5f8;
    --label-black: #1c1c1c;
    --gold: #c99a3a;
    --gold-light: #f0d58a;
    --gold-dark: #8a6420;
    --ink: #f3f0e8;
    --paper: #f4f4f2;
    --rule: #9a9a9a;
    --field-ink: #333;
  }
  * { box-sizing: border-box; margin: 0; padding: 0; }
  html, body { width: 1200px; height: 1200px; overflow: hidden; background: var(--bg); }
  .canvas { position: relative; width: 1200px; height: 1200px; }

  .label {
    position: absolute; left: 330px; top: 200px; width: 540px; height: 800px;
    background: var(--label-black);
    border: 3px solid var(--gold);
    box-shadow: 0 0 0 2px var(--label-black), 0 0 0 4px var(--gold-dark);
    color: var(--ink);
    font-family: "Old Standard TT", serif;
    text-align: center;
  }
  .label-frame {
    position: absolute; inset: 14px;
    border: 1px solid var(--gold);
    outline: 1px dotted var(--gold-dark); outline-offset: -6px;
  }
  .frame-corner {
    position: absolute; width: 22px; height: 22px; border: 2px solid var(--gold);
  }
  .frame-corner.tl { left: 8px; top: 8px; border-right: none; border-bottom: none; }
  .frame-corner.tr { right: 8px; top: 8px; border-left: none; border-bottom: none; }
  .frame-corner.bl { left: 8px; bottom: 8px; border-right: none; border-top: none; }
  .frame-corner.br { right: 8px; bottom: 8px; border-left: none; border-top: none; }

  .brand {
    position: absolute; top: 62px; left: 0; right: 0;
    display: flex; justify-content: center; align-items: center; gap: 10px;
    font-size: 17px; font-weight: 700; letter-spacing: 3px; color: var(--ink);
  }
  .brand-dot { width: 14px; height: 14px; border-radius: 50%; background: var(--ink); }

  .product-name {
    position: absolute; top: 140px; left: 0; right: 0;
    font-family: "Rye", serif; font-size: 92px; line-height: 1.05;
    background: linear-gradient(180deg, var(--gold-light), var(--gold) 55%, var(--gold-dark));
    -webkit-background-clip: text; background-clip: text; color: transparent;
  }

  .spirit-type {
    position: absolute; top: 375px; left: 0; right: 0;
    font-size: 46px; font-weight: 700; letter-spacing: 2px; color: var(--ink);
  }
  .batch {
    position: absolute; top: 432px; left: 0; right: 0;
    font-size: 20px; letter-spacing: 4px; color: var(--ink);
  }
  .mash-note {
    position: absolute; top: 478px; left: 0; right: 0;
    font-size: 12px; letter-spacing: 2px; color: var(--ink);
  }

  .handwrite-card {
    position: absolute; top: 505px; left: 60px; width: 420px; height: 150px;
    background: var(--paper);
    display: grid; grid-template-columns: 1.4fr 1fr; grid-template-rows: 1fr 1fr 1fr;
    color: var(--field-ink); font-size: 12px; text-align: left;
    border-radius: 2px;
  }
  .field { border-bottom: 1px solid var(--rule); padding: 6px 8px; }
  .field.left { border-right: 1px solid var(--rule); }
  .field.full { grid-column: 1 / 3; border-bottom: none; }

  .volume {
    position: absolute; top: 665px; right: 60px; font-size: 16px; color: var(--ink);
  }
  .maker {
    position: absolute; top: 700px; left: 0; right: 0;
    font-size: 10px; letter-spacing: 1px; line-height: 1.45; color: var(--ink);
    text-transform: uppercase;
  }
</style>
</head>
<body>
<main class="canvas">
  <section class="label">
    <div class="label-frame"></div>
    <span class="frame-corner tl"></span><span class="frame-corner tr"></span>
    <span class="frame-corner bl"></span><span class="frame-corner br"></span>

    <div class="brand"><span class="brand-dot"></span>IRON SPUR DISTILLERY</div>

    <h1 class="product-name">Ember<br>Fold</h1>

    <div class="spirit-type">WHISKEY</div>
    <div class="batch">SINGLE BATCH</div>
    <div class="mash-note">SPIRITS DISTILLED FROM MALT MASH AND HOPS</div>

    <div class="handwrite-card">
      <div class="field left">Distillate Source:</div>
      <div class="field">Alc. By Vol</div>
      <div class="field left">Aged:</div>
      <div class="field">Of:</div>
      <div class="field full">Bottled:</div>
    </div>

    <div class="volume">750ml</div>

    <div class="maker">
      Distilled and bottled by<br>
      Iron Spur Distillery LLC<br>
      14 Larch St. Cedar Vale NJ 08999
    </div>
  </section>
</main>
</body>
</html>
```